PELDRAX Business Cards

We require a business card for our company that provides IT consulting services. We already have a logo that needs to be used on the card. We want a clean professional looking design that incorporates our colours. Our main focus is providing managed services to business, which involves us looking after all of their IT requirements including managing servers/networks, projects, and procurement.

Industry/Entity Type

Information Technology

Requirements
Must have
• our logo, contact information, name, title, phone numbers

```html
<!DOCTYPE html>
<html lang="en">
<head>
<meta charset="utf-8">
<title>PELDRAX Business Cards</title>
<link href="https://fonts.googleapis.com/css2?family=Source+Sans+3:ital,wght@0,400;0,600;1,700&display=swap" rel="stylesheet">
<style>
  :root {
    --backdrop: #3d2a20;
    --brand-blue: #2a96cf;
    --brand-blue-deep: #1c76a9;
    --card-white: #ffffff;
    --ink-light: #ffffff;
  }
  * { margin: 0; padding: 0; box-sizing: border-box; }
  html, body {
    width: 1200px;
    height: 1200px;
    overflow: hidden;
    background: var(--backdrop);
    font-family: "Source Sans 3", "Segoe UI", sans-serif;
  }
  .canvas { position: relative; width: 1200px; height: 1200px; }

  .card { position: absolute; overflow: hidden; }

  /* Front */
  .card-front {
    left: 218px; top: 131px; width: 752px; height: 429px;
    background: var(--brand-blue);
  }
  .front-brand {
    position: absolute; left: 110px; top: 0; height: 100%;
    display: flex; align-items: center; gap: 22px;
    color: var(--ink-light);
  }
  .front-brand .brand-mark {
    width: 86px; height: 86px; border-radius: 50%;
    background: var(--ink-light);
  }
  .front-brand .brand-name {
    font-weight: 600; font-size: 104px; letter-spacing: 4px; line-height: 1;
  }

  /* Back */
  .card-back {
    left: 217px; top: 630px; width: 765px; height: 437px;
    background: var(--card-white);
  }
  .back-brand {
    position: absolute; right: 42px; top: 38px;
    display: flex; align-items: center; gap: 7px;
    color: var(--brand-blue);
  }
  .back-brand .brand-mark {
    width: 24px; height: 24px; border-radius: 50%;
    background: var(--brand-blue);
  }
  .back-brand .brand-name {
    font-weight: 600; font-size: 24px; letter-spacing: 1px; line-height: 1;
  }
  .info-band {
    position: absolute; left: 0; top: 109px; width: 100%; height: 219px;
    background: linear-gradient(180deg, var(--brand-blue) 0%, var(--brand-blue-deep) 100%);
    color: var(--ink-light);
  }
  .person { position: absolute; left: 84px; top: 56px; }
  .person-name { font-weight: 600; font-size: 52px; line-height: 1; letter-spacing: 0.5px; }
  .person-title { font-size: 24px; line-height: 1; margin: 4px 0 0 8px; }
  .contact { position: absolute; left: 436px; top: 58px; }
  .contact-label { font-weight: 700; font-style: italic; font-size: 25px; line-height: 0.9; }
  .contact-value { font-size: 20px; line-height: 1.05; margin-bottom: 10px; }
</style>
</head>
<body>
<div class="canvas">
  <section class="card card-front">
    <div class="front-brand">
      <span class="brand-mark"></span>
      <span class="brand-name">PELDRAX</span>
    </div>
  </section>

  <section class="card card-back">
    <div class="back-brand">
      <span class="brand-mark"></span>
      <span class="brand-name">PELDRAX</span>
    </div>
    <div class="info-band">
      <div class="person">
        <div class="person-name">YOUR NAME</div>
        <div class="person-title">job title</div>
      </div>
      <div class="contact">
        <div class="contact-label">email.</div>
        <div class="contact-value">youremail@yourdomain.com</div>
        <div class="contact-label">phone.</div>
        <div class="contact-value">123.456.7891</div>
      </div>
    </div>
  </section>
</div>
</body>
</html>
```